Create Vertical Dog Food Labels (3 inches x 5 inches) for PupKitchen

We need a packing Vertical label (3 inches x 5 inches) design for our line of Dog Food - Pup Kitchen at pupkitchenmeals.com (please review website). This design is for Custom Roll Labels. We have a logo already. Use our logo colors on label. What we need incorporated is a list of our ingredients:

50% Choice Beef
20% Pasture-raised Chicken
15% Brown Rice
15% Fresh Vegetables - Carrots, Kale, Zucchini
Herbal Health Boosters

We also need these lines at the bottom of the label:

Keeps in fridge for 4 days after thawing
Stores in freezer up to 6 months
Questions? email us at orders@meadowlanepantry.com

We have attached a sample of a competitor. The Kibble Crate.

Target Market(s)

Dog owners

Industry/Entity Type

Dog Food

Font styles to use
Sans Serif

Requirements
Must have
• Read project description above
Nice to have
• Our logo color incorporated
Should not have
• I want it simple.

```html
<!DOCTYPE html>
<html lang="en">
<head>
<meta charset="utf-8">
<title>PupKitchen – Dog Food Label</title>
<link rel="stylesheet" href="https://fonts.googleapis.com/css2?family=Outfit:wght@300;400;500;600;700&display=swap">
<style>
  :root {
    --backdrop: #5c5c5c;
    --paper: #ffffff;
    --brand-green: #0d6b0e;
    --label-green: #287f2a;
    --leaf-green: #7cbf3f;
    --band-orange: #ffa700;
    --rule: rgba(160, 210, 90, 0.55);
    --ink-light: #ffffff;
  }
  * { box-sizing: border-box; margin: 0; padding: 0; }
  html, body {
    width: 1200px; height: 1200px; overflow: hidden;
    background: var(--backdrop);
    font-family: "Outfit", sans-serif;
  }
  .label {
    position: absolute; left: 333px; top: 156px;
    width: 533px; height: 888px;
    background: var(--paper);
    overflow: hidden;
  }
  .brand {
    position: absolute; left: 0; right: 0; top: 200px; height: 72px;
    display: flex; align-items: center; justify-content: center; gap: 16px;
  }
  .brand-dot {
    width: 64px; height: 64px; border-radius: 50%;
    background: var(--leaf-green);
  }
  .brand-name {
    font-size: 42px; font-weight: 500; color: var(--brand-green);
    letter-spacing: -0.5px;
  }
  .accent-band {
    position: absolute; left: 0; right: 0; top: 438px; height: 57px;
    background: var(--band-orange);
  }
  .info-panel {
    position: absolute; left: 0; right: 0; top: 495px; bottom: 0;
    background: var(--label-green); color: var(--ink-light);
  }
  .rule {
    position: absolute; left: 67px; width: 399px; height: 0;
    border-top: 1px dashed var(--rule);
  }
  .col-divider {
    position: absolute; left: 220px; width: 0; height: 34px;
    border-left: 1px dashed var(--rule);
  }
  .ingredient {
    position: absolute; display: flex; align-items: center; gap: 10px;
  }
  .ingredient .pct { font-size: 36px; font-weight: 400; line-height: 1; letter-spacing: -0.5px; }
  .ingredient .name { font-size: 14px; font-weight: 600; line-height: 1.25; }
  .ingredient.left { right: calc(533px - 147px); }
  .ingredient.right { left: 236px; }
  .boosters {
    position: absolute; left: 0; right: 0; top: 164px;
    text-align: center; font-size: 14px; font-weight: 600;
  }
  .storage {
    position: absolute; left: 0; right: 0; top: 211px;
    text-align: center; font-size: 16px; font-weight: 300; line-height: 28px;
  }
  .divider-bar {
    position: absolute; left: 225px; top: 286px; width: 84px; height: 3px;
    border-radius: 2px; background: var(--leaf-green);
  }
  .contact {
    position: absolute; left: 0; right: 0; top: 309px; text-align: center;
  }
  .contact-heading { font-size: 18px; font-weight: 700; line-height: 26px; }
  .contact-email { font-size: 16px; font-weight: 300; line-height: 30px; }
</style>
</head>
<body>
  <main class="label">
    <div class="brand">
      <span class="brand-dot"></span>
      <span class="brand-name">PupKitchen</span>
    </div>

    <div class="accent-band"></div>

    <section class="info-panel">
      <div class="rule" style="top:21px"></div>

      <div class="ingredient left" style="top:40px">
        <span class="pct">50%</span><span class="name">Choice<br>Beef</span>
      </div>
      <div class="col-divider" style="top:40px"></div>
      <div class="ingredient right" style="top:40px">
        <span class="pct">20%</span><span class="name">Pasture-raised<br>Chicken</span>
      </div>

      <div class="rule" style="top:87px"></div>

      <div class="ingredient left" style="top:103px">
        <span class="pct">15%</span><span class="name">Brown<br>Rice</span>
      </div>
      <div class="col-divider" style="top:106px"></div>
      <div class="ingredient right" style="top:103px; left:246px">
        <span class="pct">15%</span><span class="name">Fresh Vegetables -<br>Carrots, Kale, Zucchini</span>
      </div>

      <div class="rule" style="top:153px"></div>
      <p class="boosters">Herbal Health Boosters</p>
      <div class="rule" style="top:189px"></div>

      <p class="storage">Keeps in fridge for 4 days after thawing<br>Stores in freezer up to 6 months</p>

      <div class="divider-bar"></div>

      <div class="contact">
        <p class="contact-heading">Questions? email us at:</p>
        <p class="contact-email">orders@meadowlanepantry.com</p>
      </div>
    </section>
  </main>
</body>
</html>
```